Non Profit Organization Holiday Card (Paper and Electronic)

We are a non profit that trains teachers in a method for teaching writing to kids ages 8-18. We would like two versions of a Christmas card. One version should be a PDF to fit in a 5x7 envelope. We are hoping that a second version could be coded in Brightwave Mailer to be sent via email.
The text should read
Happy Holidays
From all of us at
The Penmark Alliance
Our logo should be included somewhere. The rest of the attachments (as well as our style guide) are optional in case they support the design, which we would like to be relatively simple.

```html
<!DOCTYPE html>
<html lang="en">
<head>
<meta charset="utf-8">
<title>Happy Holidays – The Penmark Alliance</title>
<link rel="stylesheet" href="https://fonts.googleapis.com/css2?family=Damion&family=Barlow:wght@500&family=Crimson+Text:ital@1&display=swap">
<style>
  :root {
    --backdrop: #e4e4e2;
    --navy: #0b3480;
    --royal: #1f62c4;
    --sky: #3a86dc;
    --snow: #ffffff;
    --berry: #cf2027;
    --amber: #f08a1c;
    --ink: #1b1b1b;
    --brand-blue: #1d5fb5;
    --pine: #3f8a3a;
  }
  * { margin: 0; padding: 0; box-sizing: border-box; }
  html, body {
    width: 1200px;
    height: 817px;
    overflow: hidden;
    background: var(--backdrop);
  }
  .card {
    position: absolute;
    left: 330px;
    top: 28px;
    width: 540px;
    height: 760px;
    overflow: hidden;
    background: radial-gradient(ellipse at 50% 55%, var(--sky) 0%, var(--royal) 40%, var(--navy) 100%);
  }
  .garland {
    position: absolute;
    left: 0;
    top: 0;
    width: 540px;
    height: 190px;
    background: linear-gradient(180deg, var(--pine) 0%, rgba(63,138,58,0.55) 35%, rgba(31,98,196,0) 100%);
  }
  .strings {
    position: absolute;
    left: 0;
    top: 0;
  }
  .greeting {
    position: absolute;
    left: 0;
    top: 188px;
    width: 540px;
    text-align: center;
    font-family: "Damion", cursive;
    color: var(--snow);
    line-height: 0.98;
  }
  .greeting .line-one { display: block; font-size: 96px; margin-left: -30px; }
  .greeting .line-two { display: block; font-size: 100px; margin-left: 20px; }
  .snowfield {
    position: absolute;
    left: 0;
    bottom: 0;
  }
  .quote-badge {
    position: absolute;
    left: 15px;
    top: 413px;
    width: 234px;
    height: 234px;
    border-radius: 50%;
    background: var(--berry);
    color: var(--snow);
    font-family: "Barlow", sans-serif;
    font-weight: 500;
    font-size: 18px;
    line-height: 1.28;
    text-align: center;
    display: flex;
    flex-direction: column;
    justify-content: center;
    padding: 0 30px;
  }
  .quote-badge .mark { font-size: 26px; line-height: 0; vertical-align: -4px; }
  .quote-badge cite {
    display: block;
    font-style: normal;
    margin-top: 24px;
  }
  .photo {
    position: absolute;
    border-radius: 50%;
    border: 3px solid var(--amber);
  }
  .photo-tutoring {
    left: 329px;
    top: 395px;
    width: 158px;
    height: 158px;
    background: radial-gradient(circle at 45% 55%, #e8c25a 0%, #b98a5c 35%, #f1ede6 80%);
  }
  .photo-reading {
    left: 418px;
    top: 548px;
    width: 114px;
    height: 114px;
    background: radial-gradient(circle at 45% 60%, #8a6a58 0%, #c7b8a6 45%, #eef0ea 85%);
  }
  .signoff {
    position: absolute;
    left: 20px;
    top: 688px;
    display: flex;
    align-items: center;
    gap: 16px;
  }
  .signoff-lead {
    font-family: "Crimson Text", serif;
    font-style: italic;
    font-size: 29px;
    color: var(--ink);
  }
  .brand {
    display: flex;
    align-items: center;
    gap: 8px;
  }
  .brand-dot {
    width: 14px;
    height: 14px;
    border-radius: 50%;
    background: var(--brand-blue);
  }
  .brand-name {
    font-family: "Barlow", sans-serif;
    font-weight: 500;
    font-size: 22px;
    color: var(--brand-blue);
    white-space: nowrap;
  }
</style>
</head>
<body>
  <main class="card">
    <div class="garland" role="img" aria-label="Holly garland with red berries and hanging red and gold baubles"></div>

    <svg class="strings" width="540" height="560" viewBox="0 0 540 560" aria-hidden="true">
      <line x1="404" y1="0" x2="404" y2="396" stroke="var(--amber)" stroke-width="3" stroke-dasharray="4 2"/>
      <line x1="467" y1="0" x2="467" y2="549" stroke="var(--amber)" stroke-width="3" stroke-dasharray="4 2"/>
    </svg>

    <h1 class="greeting">
      <span class="line-one">Happy</span>
      <span class="line-two">Holidays</span>
    </h1>

    <svg class="snowfield" width="540" height="160" viewBox="0 0 540 160" aria-hidden="true">
      <path d="M0 40 Q40 18 80 34 T170 30 T260 22 T350 30 T440 20 T540 24 L540 160 L0 160 Z" fill="var(--snow)"/>
    </svg>

    <blockquote class="quote-badge">
      <p><span class="mark">“</span>The Penmark Alliance helps me think about what we are learning.<span class="mark">”</span></p>
      <cite>- Marisol, pd. 2</cite>
    </blockquote>

    <div class="photo photo-tutoring" role="img" aria-label="Photo of a teacher helping a student write at a classroom desk"></div>
    <div class="photo photo-reading" role="img" aria-label="Photo of a teacher and student working together on a writing task"></div>

    <footer class="signoff">
      <span class="signoff-lead">From all of us at</span>
      <span class="brand">
        <span class="brand-name">The Penmark Alliance</span>
        <span class="brand-dot"></span>
      </span>
    </footer>
  </main>
</body>
</html>
```